Lunaryth needs a elegant mystical business card design

The theme of Lunaryth is centered on Kemetic/Ancient Egyptian Spirituality. My business sells handmade scented candles, mystic oils, body sprays, tarot readings and more. I would like my business card to reflect an elegant and mystical look. Hieroglyphs around the borders would be a cool idea. Also, the main colors I am working with is Black and Gold= colors of royalty. Black background. The business card will be double sided. The back will have the logo, and the front will have the basic information (ie name, title, business, phone, email, website, etc..)

Target Market(s)

The target market are people into metaphysics, holistic healing, ancient Egyptian culture, aromatherapy, occult science, and the esoteric.

Industry/Entity Type

Business

Contact Information for Business Card

Name: Marisol T. Pike
Title: Owner
Business: LUNARYTH
Phone: 555.210.4473
Website: www.Lunaryth.example
Facebook, Instagram, and twitter icons

Font styles to use
Serif
Decorative

Requirements
Must have
• My logo, and website.
Nice to have
• Ancient Egyptian hieroglyphs, Elegant designs around the border, or encircling the logo.

```html
<!DOCTYPE html>
<html lang="en">
<head>
<meta charset="utf-8">
<title>Lunaryth Business Card</title>
<link href="https://fonts.googleapis.com/css2?family=Cinzel:wght@500&family=Cormorant+Garamond:wght@500&display=swap" rel="stylesheet">
<style>
  :root {
    --backdrop: #3b3a3a;
    --card: #08080a;
    --gold: #c9a14a;
    --gold-soft: #a98433;
    --gold-deep: #6e5320;
  }
  * { margin: 0; padding: 0; box-sizing: border-box; }
  html, body { width: 1200px; height: 1000px; overflow: hidden; }
  body {
    background: var(--backdrop);
    display: flex;
    flex-direction: column;
    align-items: center;
    justify-content: center;
    gap: 70px;
  }
  .card {
    width: 620px;
    height: 354px;
    background: var(--card);
    border-radius: 26px;
    position: relative;
    box-shadow: 0 18px 40px rgba(0,0,0,0.45);
  }
  .brand {
    position: absolute;
    display: flex;
    align-items: center;
    gap: 14px;
    font-family: "Cinzel", serif;
    font-weight: 500;
    color: var(--gold);
    letter-spacing: 0.12em;
  }
  .brand-dot {
    width: 12px; height: 12px;
    border-radius: 50%;
    background: var(--gold);
  }
  .card-back .brand {
    left: 50%; top: 50%;
    transform: translate(-50%, -50%);
    font-size: 40px;
  }
  .card-front .brand {
    left: 60px; top: 50%;
    transform: translateY(-50%);
    font-size: 32px;
  }
  .divider {
    position: absolute;
    left: 340px; top: 70px;
    width: 2px; height: 150px;
    background: linear-gradient(to bottom, transparent, var(--gold), transparent);
  }
  .contact {
    position: absolute;
    left: 372px; top: 70px;
    font-family: "Cormorant Garamond", serif;
    font-weight: 500;
    color: var(--gold);
  }
  .contact-name { font-size: 22px; letter-spacing: 0.03em; }
  .contact-title { font-size: 17px; color: var(--gold-soft); margin-top: 2px; }
  .contact-lines { margin-top: 34px; display: grid; gap: 10px; font-size: 19px; }
  .contact-line { display: flex; align-items: center; gap: 12px; }
  .contact-line svg { width: 16px; height: 18px; flex: none; }
  .social {
    position: absolute;
    right: 48px; bottom: 80px;
    display: flex; gap: 12px;
  }
  .social-slot {
    width: 28px; height: 28px;
    border-radius: 5px;
    background: linear-gradient(135deg, var(--gold), var(--gold-deep));
  }
</style>
</head>
<body>
  <section class="card card-back" aria-label="Card back">
    <div class="brand"><span class="brand-dot"></span>LUNARYTH</div>
  </section>

  <section class="card card-front" aria-label="Card front">
    <div class="brand"><span class="brand-dot"></span>LUNARYTH</div>
    <div class="divider"></div>
    <div class="contact">
      <p class="contact-name">Marisol T. Pike</p>
      <p class="contact-title">Owner</p>
      <div class="contact-lines">
        <p class="contact-line">
          <svg viewBox="0 0 16 18" aria-hidden="true"><rect x="3" y="1" width="10" height="16" rx="2" fill="none" stroke="#c9a14a" stroke-width="1.6"/><line x1="7" y1="14" x2="9" y2="14" stroke="#c9a14a" stroke-width="1.6"/></svg>
          555.210.4473
        </p>
        <p class="contact-line">
          <svg viewBox="0 0 16 18" aria-hidden="true"><rect x="1" y="3" width="14" height="10" rx="1.5" fill="none" stroke="#c9a14a" stroke-width="1.6"/><line x1="5" y1="16" x2="11" y2="16" stroke="#c9a14a" stroke-width="1.6"/></svg>
          www.Lunaryth.example
        </p>
      </div>
    </div>
    <div class="social" aria-label="Social media profiles">
      <span class="social-slot"></span>
      <span class="social-slot"></span>
      <span class="social-slot"></span>
    </div>
  </section>
</body>
</html>
```